Daddy's Hour Classes for new fathers

I need a flyer for new dads that will appeal to new dads to come to a 2-hr class about fatherhood and child development.

I am a therapist and educator and I run classes for dads.

I will need to over lay some text over the flyer regarding the details of where and when the class is.

In essence the Flyer needs to promote:
"Daddy's Hour" in bold and large lettering
with 'TM" the trademark symbol beside it in small font and up beside "Daddys Hour".

Here is the text required - it's also on a file uploaded!:
Daddy’s Hour TM – getting into fatherhood

New-Father classes for dads and dads-to-be, run by Ned Brannock

What you’ll get from the 2-hour class:
• Baby-basics - a simple way to understand how to know what your baby needs
• Bonding with your baby
• How to nurture your baby’s developing brain during the biggest period of brain-growth.
• How to give your child the twin-benefits of an attachment system.
• How to make the Work-Life-Relationship balance work after a baby!
• Strategies for managing stress.
Plus hearing from other dads.

About the presenter
The daddy’s hour classes are run by Edward Brannock, a fathers-educator who has run classes for dads for more than 10 years. He is a father of two and has consults around fatherhood issues. He has also presented at conferences and trains midwives and maternal child health nurses on father-inclusive practice Ned has also appeared on tv and radio and in print around the topic of fatherhood..
and his work has can be found on: http://growingkidsplace.example.au/pa_notes_expecting/pa_notes_on_expecting.html a & www.papacheckin.example.au/

Feedback from dads:
"Very impressed - exceeded expectations."
"Some things tonight I had never considered. Helping in later child development, looking at things from different angles."
"The discussion on brain development - the way it was explained - it's good, I would recommend it to others."

Enrol now at: www.edwardbrannock.example.au/daddys-hour.html

www.edwardbrannock.example.au/daddys-hour

THANKS FOR YOUR INTEREST - LOOK FORWARD TO SEEING YOUR GREAT WORK!

Target Market(s)

Dads and dads-to-be who want to learn more about fatherhood so that they get off to a great start as a dad.

Industry/Entity Type

Health

Requirements
Nice to have
• If you think it's too text heavy, ditch the text and I can put it on the website.

Go with your creative instinct!

```html
<!DOCTYPE html>
<html lang="en">
<head>
<meta charset="utf-8">
<title>Daddy's Hour – Classes for new dads</title>
<link rel="stylesheet" href="https://fonts.googleapis.com/css2?family=Source+Sans+3:wght@400;600&display=swap">
<style>
  :root {
    --page: #ffffff;
    --slate-dark: #26333c;
    --slate: #3a4952;
    --slate-light: #4d5d67;
    --sky: #9fd4e3;
    --sky-soft: #bfe3ec;
    --ink-light: #ffffff;
    --ink-muted: #d9e3e8;
    --photo-warm: #d9cfc6;
    --photo-cool: #a9b9c6;
  }
  * { box-sizing: border-box; margin: 0; padding: 0; }
  html, body {
    width: 1200px; height: 1200px; overflow: hidden;
    background: var(--page);
    font-family: "Source Sans 3", "Myriad Pro", sans-serif;
  }
  .flyer {
    position: absolute; left: 219px; top: 52px;
    width: 774px; height: 1084px;
    background: radial-gradient(ellipse at 50% 70%, var(--slate-light), var(--slate) 55%, var(--slate-dark));
    overflow: hidden;
    color: var(--ink-light);
  }
  .flyer-shapes { position: absolute; inset: 0; }
  .brand { position: absolute; left: 40px; top: 52px; }
  .brand-name {
    font-size: 50px; font-weight: 600; line-height: 1; color: var(--ink-light);
  }
  .brand-tagline { font-size: 26px; font-weight: 400; color: var(--sky); margin-top: 8px; margin-left: 96px; }
  .stork-art {
    position: absolute; left: 500px; top: 20px; width: 250px; height: 190px;
    background: radial-gradient(closest-side, var(--sky-soft), rgba(191,227,236,0.35) 55%, rgba(159,212,227,0));
  }
  .feedback-bubble {
    position: absolute; left: 516px; top: 548px; width: 250px; height: 210px;
  }
  .feedback-text {
    position: absolute; left: 556px; top: 586px; width: 172px;
    text-align: center; font-size: 14.5px; line-height: 1.3; color: var(--ink-light);
  }
  .feedback-source { display: block; margin-top: 8px; font-size: 12.5px; color: var(--ink-muted); }
  .class-intro { position: absolute; left: 40px; top: 712px; width: 290px; }
  .class-heading { font-size: 28px; font-weight: 600; line-height: 1.0; width: 280px; }
  .class-heading .presenter { color: var(--sky); }
  .presenter-bio { margin-top: 20px; width: 255px; font-size: 14.5px; line-height: 1.3; color: var(--ink-muted); }
  .presenter-bio p + p { margin-top: 20px; }
  .class-gains { position: absolute; left: 354px; top: 766px; width: 410px; }
  .gains-heading { font-size: 19px; font-weight: 600; color: var(--sky); white-space: nowrap; }
  .gains-list { list-style: none; margin-top: 16px; font-size: 12.5px; line-height: 1; color: var(--ink-muted); }
  .gains-list li { margin-bottom: 13px; white-space: nowrap; }
  .gains-list li::before { content: "- "; }
  .enrol { margin-top: 24px; font-size: 15px; font-weight: 600; color: var(--sky); white-space: nowrap; letter-spacing: -0.2px; }
</style>
</head>
<body>
<main class="flyer">
  <svg class="flyer-shapes" viewBox="0 0 774 1084" width="774" height="1084">
    <defs>
      <linearGradient id="photoTone" x1="0" y1="0" x2="1" y2="0">
        <stop offset="0" stop-color="var(--photo-cool)"/>
        <stop offset="0.55" stop-color="var(--photo-warm)"/>
        <stop offset="1" stop-color="#cfc8c4"/>
      </linearGradient>
    </defs>
    <path role="img" aria-label="Photo: a new father cradling his newborn baby, mother resting in a hospital bed behind"
          d="M0,222 C200,250 460,232 774,178 L774,598 C560,650 300,690 0,660 Z" fill="url(#photoTone)"/>
    <path d="M0,222 C200,250 460,232 774,178" fill="none" stroke="var(--sky)" stroke-width="5"/>
    <path d="M0,660 C300,690 560,650 774,598" fill="none" stroke="var(--sky)" stroke-width="5"/>
  </svg>

  <header class="brand">
    <h1 class="brand-name">Daddy’s Hour</h1>
    <p class="brand-tagline">Classes for new dads</p>
  </header>

  <div class="stork-art" role="img" aria-label="Illustration: a stork flying with a bundled baby"></div>

  <svg class="feedback-bubble" viewBox="0 0 250 210" aria-hidden="true">
    <path d="M125,8 C190,8 242,48 242,96 C242,146 190,184 125,184 C110,184 96,182 84,178 L22,204 L50,160 C22,144 8,122 8,96 C8,48 60,8 125,8 Z"
          fill="var(--slate)" stroke="var(--sky)" stroke-width="2"/>
  </svg>
  <blockquote class="feedback-text">
    “Some things tonight I had never considered. Helping in later child development, looking at things from different angles”
    <span class="feedback-source">Genuine Father Feedback</span>
  </blockquote>

  <section class="class-intro">
    <h2 class="class-heading">New Father classes for dads &amp; dads-to-be run by <span class="presenter">Ned Brannock</span></h2>
    <div class="presenter-bio">
      <p>The daddy’s hour classes are run by Edward Brannock, a fathers-educator who has run classes for dads for more than 10 years.</p>
      <p>He is a father of two and has consults around fatherhood issues. He has also presented at conferences and trains midwives and maternal child health nurses on father-inclusive practice.</p>
      <p>Ned has also appeared on tv and radio and in print around the topic of fatherhood.</p>
    </div>
  </section>

  <section class="class-gains">
    <h3 class="gains-heading">What you will gain from our two hour class;</h3>
    <ul class="gains-list">
      <li>Baby-basics: A simple way to understand what your baby needs.</li>
      <li>Bonding with your baby.</li>
      <li>How to nuture your baby’s developing brain.</li>
      <li>How to give your child the twin-benefits of an attachment system.</li>
      <li>How to manage your work-life-relationship balance after a baby.</li>
      <li>Strategies for managing stress.</li>
      <li>Plus the added benefit of networking with other dads and dads-to-be.</li>
    </ul>
    <p class="enrol">Enrol now at: www.edwardbrannock.example.au/daddys-hour</p>
  </section>
</main>
</body>
</html>
```